8-seitige Frühlingsbroschüre
Zielgruppe
Immobilien
Immobilienkäufer / Immobilienverkäufer
Aufgabenstellung
Frühlingsflyer.
Z.b. Frühling! Zeit für Wachstum und Neues oder Jeder Frühling trägt den Zauber eines Anfangs in sich! Lassen auch Sie sich verzaubern!
Es sollte auch unsere Farben vorhanden sein, aber auch zum Frühling passen.
Das Blau und Gold etwas dezenter, nicht so vollflächig. Mehr weiß. Dann kann man auch den Frühling (Blumen/Farben) besser einbringen.
Format: Din A4, 8 Seitige Broschüre (4 Blätter)
Vorderseite: Lind-Immobilien Wenkhuber, (z.B. Seit vielen Jahren sind Immobilien unsere Leidenschaft)
Ihr Immobilienmakler in der Region
2+3 Seite: Neubauprojekt 'Vogtlandstr. Gaildorf', 9 Neubauwohnungen
4+5 Seite: Weitere Objket Angebote
6 Seite: Wir suchen folgende Objekt für vorgemerkte Kunden
7 Seite: Home Staging (bitte Vorher- Nachher Bilder)
8 Seite: Unser Angebot, unsere Leistungen,
Ich lade Dateien hoch von vorhandenen Printsachen, Logo, Texte
Z.b Bilder die mir gefallen: Fotaro Pool: 258017364, 47180325, 173526048, 109684213

```html
<!DOCTYPE html>
<html lang="de">
<head>
<meta charset="utf-8">
<title>Wohnträume und Lebensräume – Doppelseite</title>
<link href="https://fonts.googleapis.com/css2?family=Fira+Sans+Condensed:wght@300;400;500;600&display=swap" rel="stylesheet">
<style>
  :root {
    --backdrop: #e4e5e7;
    --paper: #ffffff;
    --gold: #b8963c;
    --navy: #1f3763;
    --blue: #3d68a8;
    --fold: #e9e9ea;
  }
  * { margin: 0; padding: 0; box-sizing: border-box; }
  html, body { width: 1200px; height: 900px; overflow: hidden; background: var(--backdrop); }
  body { font-family: "Fira Sans Condensed", "Arial Narrow", sans-serif; color: var(--navy); }

  .spread {
    position: absolute; left: 60px; top: 68px; width: 1080px; height: 764px;
    display: flex; box-shadow: 0 6px 24px rgba(0,0,0,0.12);
  }
  .page { position: relative; width: 540px; height: 764px; background: var(--paper); }
  .page--left { background: linear-gradient(to right, var(--paper) 92%, var(--fold)); }
  .page--right { background: linear-gradient(to left, var(--paper) 94%, var(--fold)); }

  .photo { position: absolute; }

  /* left page */
  .page-title {
    position: absolute; left: 46px; top: 120px;
    font-weight: 400; font-size: 34px; line-height: 1.08; letter-spacing: 0.5px;
    color: var(--gold); text-transform: uppercase;
  }
  .page-subtitle {
    position: absolute; left: 48px; top: 206px;
    font-size: 12.5px; font-weight: 500; letter-spacing: 0.6px; color: var(--blue);
    text-transform: uppercase;
  }
  .feature { position: absolute; left: 300px; top: 250px; width: 205px; }
  .feature-title {
    font-size: 12.5px; font-weight: 600; color: var(--blue); text-transform: uppercase;
    letter-spacing: 0.3px; margin-bottom: 10px;
  }
  .feature p { font-size: 10px; line-height: 1.65; color: var(--gold); font-weight: 300; margin-bottom: 10px; }
  .feature p strong { font-weight: 600; color: var(--gold); }
  .price { font-size: 10px; font-weight: 600; color: var(--navy); margin-top: 14px; }
  .price-note { font-size: 6.5px; font-weight: 500; color: var(--navy); line-height: 1.35; margin-top: 5px; text-transform: uppercase; }

  .more { position: absolute; left: 62px; top: 565px; width: 240px; }
  .more-title { font-size: 12px; font-weight: 600; color: var(--blue); text-transform: uppercase; margin-bottom: 8px; }
  .more p { font-size: 10px; line-height: 1.55; color: var(--gold); font-weight: 300; }
  .more .url { margin-top: 12px; text-align: right; }

  /* right page */
  .listing { position: absolute; width: 225px; }
  .listing-title {
    font-size: 11.5px; font-weight: 600; color: var(--navy); text-transform: uppercase;
    letter-spacing: 0.2px; line-height: 1.3; margin-bottom: 10px;
  }
  .listing p { font-size: 9.5px; line-height: 1.65; color: var(--gold); font-weight: 300; }
  .listing .price { font-size: 9.5px; margin-top: 14px; }
  .company { font-size: 9.5px; font-weight: 600; color: var(--navy); text-transform: uppercase; margin-top: 18px; margin-bottom: 4px; }
  .contact { font-size: 9.5px; line-height: 1.6; color: var(--gold); font-weight: 300; }
</style>
</head>
<body>
<main class="spread">
  <section class="page page--left">
    <h1 class="page-title">Wohnträume und<br>Lebensräume</h1>
    <p class="page-subtitle">Zeitgemässes und trendiges Wohnen</p>

    <div class="photo" role="img" aria-label="Heller Wohnraum mit weißem Sideboard, Fernseher, Orchidee und Holzboden"
         style="left:40px; top:250px; width:250px; height:265px; background:linear-gradient(160deg,#efe5d6 0%,#f4f1ec 45%,#e6d6bd 80%,#c9a77a 100%);"></div>

    <article class="feature">
      <h2 class="feature-title">Wohntraum für die ganze Familie</h2>
      <p>In dieser sehr schönen und großzügigen Maisonette-Wohnung in einer ruhigen Wohngegend in <strong>Schwäbisch Hall-Teuersdorf</strong> wartet das Lebensglück auf die anspruchsvolle Familie.</p>
      <p>Sowohl die hochwertige Ausstattung (Echtholztreppe, Laminat- oder Fliesenbelag, etc.) als auch die gute Infrastruktur versprechen familienfreundliches und doch gut angebundenes Wohnen.</p>
      <div class="price">244.900,00 € | 5 ZIMMER | 105 M²</div>
      <div class="price-note">zzgl. 10.500 € Tiefgaragenstellplatz bzw.<br>3.500 € Aussenstellplatz</div>
    </article>

    <div class="more">
      <h2 class="more-title">Weitere Lebens(t)räume...</h2>
      <p>... ganz gleich ob für Familien, Singles oder Verliebte finden sie auf unserer Website</p>
      <p class="url">https://lind-wenkhuber.de</p>
    </div>

    <div class="photo" role="img" aria-label="Heller Raum mit gemustertem Ohrensessel in Orange und Stehlampe"
         style="left:320px; top:540px; width:170px; height:160px; background:linear-gradient(150deg,#f3f2f0 0%,#e9e6e1 50%,#c7824a 75%,#dcd6cd 100%);"></div>
  </section>

  <section class="page page--right">
    <div class="photo" role="img" aria-label="Dunkles Einfamilienhaus mit roter Tür unter blauem Himmel, Rasen davor"
         style="left:25px; top:265px; width:235px; height:122px; background:linear-gradient(180deg,#3f7fd0 0%,#7fb0e6 40%,#4a2c25 62%,#6a8f3e 100%);"></div>
    <article class="listing" style="left:272px; top:280px; width:235px;">
      <h2 class="listing-title">Die beste Kombi aus zwei Welten</h2>
      <p>Dieses Top energetisches Einfamilienhaus wartet mit einer modernen (behindertenfreundlichen) Einliegerwohnung und einer Gewerbeeinheit auf.</p>
      <div class="price">559.000,00 € | 7 ZIMMER | 347 M²</div>
    </article>

    <article class="listing" style="left:28px; top:410px; width:225px;">
      <h2 class="listing-title">Wohnen und Arbeiten unter einem Dach</h2>
      <p>Das komplette Areal bietet 3 Wohneinheiten und eine große Gewerbeeinheit mit Ausstellungsraum, Empfang und mehreren Lagerräumen.</p>
      <div class="price">739.000,00 € | 3 WOHNEINHEITEN | 618,00 M²</div>
    </article>
    <div class="photo" role="img" aria-label="Weißes Gewerbegebäude mit Balkonen und Parkplatz davor"
         style="left:263px; top:398px; width:234px; height:120px; background:linear-gradient(180deg,#c4d6ea 0%,#e8edf2 45%,#d7d8da 70%,#6a6d72 100%);"></div>

    <div class="photo" role="img" aria-label="Geöffnete Holztür mit Schlüssel im Schloss vor grünem, unscharfem Garten"
         style="left:25px; top:530px; width:237px; height:175px; background:linear-gradient(90deg,#8fc24a 0%,#b5d873 40%,#6b5a2a 62%,#8a7338 100%);"></div>
    <article class="listing" style="left:274px; top:543px; width:235px;">
      <h2 class="listing-title">Wohnen und/oder Arbeiten<br>mit Persönlichkeit</h2>
      <p>Die geeigneten Immobilienobjekte dafür finden wir für Sie. Melden Sie sich bei</p>
      <div class="company">Lind-Immobilien Wenkhuber GmbH</div>
      <div class="contact">Miriam und Jonas Wenkhuber<br>info@lind-wenkhuber.de<br>+49 7961 482730 | +49 1577 2986413</div>
    </article>
  </section>
</main>
</body>
</html>
```